Sign listing benefits of Wash and Fold Service

Sign 48 inches wide and 24 inches height to showcase service listed above.
Benefits include:
Saves Money
Saves Time
Convenient
Stain Treatment

Looking for something colorful (Blue and white are our business colors) the look of a laundromat business.

```html
<!DOCTYPE html>
<html lang="en">
<head>
<meta charset="UTF-8">
<title>Benefits of Wash and Dry Fold – Sign</title>
<link rel="stylesheet" href="https://fonts.googleapis.com/css2?family=Montserrat:wght@700;800&display=swap">
<style>
  :root {
    --page-bg: #c9c9c9;
    --sky-light: #aeeafc;
    --sky-mid: #4cc0ea;
    --sky-deep: #1a9fdb;
    --royal: #0d4fc4;
    --royal-dark: #0a3fb0;
    --azure: #2c8ee8;
    --white: #ffffff;
    --text-shade: rgba(10, 40, 90, 0.55);
  }
  * { box-sizing: border-box; margin: 0; padding: 0; }
  html, body {
    width: 1200px; height: 1200px; overflow: hidden;
    background: var(--page-bg);
    font-family: "Montserrat", Arial, sans-serif;
  }
  .sign {
    position: absolute; left: 71px; top: 340px;
    width: 1055px; height: 525px; overflow: hidden;
    background: radial-gradient(ellipse 500px 340px at 530px 255px, var(--sky-light) 0%, var(--sky-mid) 55%, var(--sky-deep) 100%);
  }
  .sign-art { position: absolute; inset: 0; width: 100%; height: 100%; }
  .silver-text {
    color: var(--white);
    background: linear-gradient(180deg, var(--white) 0%, var(--white) 45%, #cfd6de 60%, var(--white) 100%);
    -webkit-background-clip: text; background-clip: text;
    -webkit-text-fill-color: transparent;
    filter: drop-shadow(1px 2px 1px var(--text-shade));
    text-transform: uppercase;
    white-space: nowrap;
    line-height: 1;
  }
  .headline-top {
    position: absolute; left: 129px; top: 54px;
    font-size: 46px; font-weight: 800;
  }
  .headline-band {
    position: absolute; left: 0; top: 106px; width: 615px; height: 54px;
    border-radius: 0 27px 27px 0;
    background: linear-gradient(90deg, var(--royal-dark) 0%, var(--royal) 60%, var(--azure) 100%);
  }
  .headline-main {
    position: absolute; left: 48px; top: 109px;
    font-size: 44px; font-weight: 800;
  }
  .benefit-list { position: absolute; left: 47px; top: 173px; list-style: none; }
  .benefit { display: flex; align-items: center; height: 50px; }
  .benefit-tick { width: 39px; height: 39px; margin-right: 15px; flex: none; }
  .benefit-label { font-size: 39px; font-weight: 700; line-height: 50px; }
  .call-label {
    position: absolute; left: 96px; top: 428px;
    font-size: 26px; font-weight: 700;
  }
  .call-row {
    position: absolute; left: 42px; top: 453px; height: 52px;
    display: flex; align-items: center;
  }
  .call-icon { width: 41px; height: 41px; margin-right: 10px; }
  .call-number { font-size: 49px; font-weight: 800; }
  .photo-area {
    position: absolute; left: 618px; top: 27px; width: 380px; height: 498px;
    border-radius: 190px 190px 0 0;
    background: linear-gradient(180deg, rgba(160, 220, 240, 0.55) 0%, rgba(230, 240, 245, 0.7) 55%, rgba(200, 215, 225, 0.75) 100%);
  }
</style>
</head>
<body>
  <section class="sign" aria-label="Benefits of wash and dry fold sign">
    <svg class="sign-art" viewBox="0 0 1055 525" aria-hidden="true">
      <defs>
        <linearGradient id="footer-fill" x1="0" y1="0" x2="1" y2="0">
          <stop offset="0" stop-color="#0a3fb0"/>
          <stop offset="0.6" stop-color="#2c8ee8"/>
          <stop offset="1" stop-color="#1d6fd8"/>
        </linearGradient>
        <linearGradient id="silver-edge" x1="0" y1="0" x2="1" y2="0">
          <stop offset="0" stop-color="#9aa3ad"/>
          <stop offset="0.35" stop-color="#f4f6f8"/>
          <stop offset="0.7" stop-color="#b7bec6"/>
          <stop offset="1" stop-color="#8d959e"/>
        </linearGradient>
      </defs>
      <path d="M0 428 C80 400 150 392 240 396 C380 404 520 450 624 462 C780 478 960 450 1055 388 L1055 525 L0 525 Z" fill="url(#silver-edge)"/>
      <path d="M0 440 C80 412 150 404 240 408 C380 416 520 462 624 474 C780 490 960 462 1055 424 L1055 525 L0 525 Z" fill="url(#footer-fill)"/>
    </svg>

    <div class="photo-area" role="img" aria-label="Photo of a smiling woman holding a stack of freshly folded towels and clothes"></div>

    <p class="headline-top silver-text">Benefits of</p>
    <div class="headline-band"></div>
    <h1 class="headline-main silver-text">Wash and Dry Fold</h1>

    <ul class="benefit-list">
      <li class="benefit">
        <svg class="benefit-tick" viewBox="0 0 40 40" aria-hidden="true"><circle cx="20" cy="20" r="17" fill="none" stroke="#0d4fc4" stroke-width="3.5"/><path d="M11 20 L18 27 L33 9" fill="none" stroke="#0d4fc4" stroke-width="4" stroke-linecap="round" stroke-linejoin="round"/></svg>
        <span class="benefit-label silver-text">Saves Money</span>
      </li>
      <li class="benefit">
        <svg class="benefit-tick" viewBox="0 0 40 40" aria-hidden="true"><circle cx="20" cy="20" r="17" fill="none" stroke="#0d4fc4" stroke-width="3.5"/><path d="M11 20 L18 27 L33 9" fill="none" stroke="#0d4fc4" stroke-width="4" stroke-linecap="round" stroke-linejoin="round"/></svg>
        <span class="benefit-label silver-text">Saves Time</span>
      </li>
      <li class="benefit">
        <svg class="benefit-tick" viewBox="0 0 40 40" aria-hidden="true"><circle cx="20" cy="20" r="17" fill="none" stroke="#0d4fc4" stroke-width="3.5"/><path d="M11 20 L18 27 L33 9" fill="none" stroke="#0d4fc4" stroke-width="4" stroke-linecap="round" stroke-linejoin="round"/></svg>
        <span class="benefit-label silver-text">Convenient</span>
      </li>
      <li class="benefit">
        <svg class="benefit-tick" viewBox="0 0 40 40" aria-hidden="true"><circle cx="20" cy="20" r="17" fill="none" stroke="#0d4fc4" stroke-width="3.5"/><path d="M11 20 L18 27 L33 9" fill="none" stroke="#0d4fc4" stroke-width="4" stroke-linecap="round" stroke-linejoin="round"/></svg>
        <span class="benefit-label silver-text">Stain Treatment</span>
      </li>
    </ul>

    <p class="call-label silver-text">Call us:</p>
    <div class="call-row">
      <svg class="call-icon" viewBox="0 0 44 44" aria-hidden="true">
        <circle cx="22" cy="22" r="21" fill="#f4f6f8"/>
        <path d="M14 11 l5 -1 l3 7 l-3 3 q3 6 8 9 l3 -3 l7 3 l-1 5 q-2 3 -6 2 q-12 -4 -18 -18 q-1 -5 2 -7 z" fill="#0d4fc4"/>
      </svg>
      <span class="call-number silver-text">000.000.000</span>
    </div>
  </section>
</body>
</html>
```